Adapt a PowerPoint presentation to new Template

We have a new powerpoint template that we would like to adapt to our old powerpoint base presentation. I can share the old base template that is populated with information and data that needs to be adapted and "beautified" to the new template. I have all the source files necessary. Need to adapt the Larkfield Partners presentation to RWP Template. Meaning, to have the presentation look like the RWP template with no prior Larkfield template scheme's (coloring, logos, font, etc)

I will be making a decision by Wednesday, October 20th, 2021

Target Market(s)

Professionals

Requirements
Must have
• Adaption to our RWP Template
Nice to have
• Fully utilized tables, graphs, and graphics
Should not have
• Any Larkfield Partners Template palate

```html
<!DOCTYPE html>
<html lang="en">
<head>
<meta charset="utf-8">
<title>RWP – Quarter 2, 2021</title>
<link href="https://fonts.googleapis.com/css2?family=Open+Sans:wght@400;600;700;800&display=swap" rel="stylesheet">
<style>
:root{
  --teal:#4f9e93;
  --teal-light:#5aac9c;
  --teal-mid:#458a80;
  --navy:#1f5b8c;
  --blue:#1a80b8;
  --ink:#222;
  --red:#e0181e;
  --canvas:#ffffff;
}
*{box-sizing:border-box;margin:0;padding:0}
html,body{width:686px;height:1200px;overflow:hidden;background:var(--canvas);font-family:"Open Sans",Arial,sans-serif;color:var(--ink)}
.slide{position:absolute;left:89px;width:509px;height:280px;background:#fff;box-shadow:0 1px 3px rgba(0,0,0,.18);overflow:hidden}
.slide--title{top:7px}
.slide--budget{top:303px}
.slide--cash{top:598px}
.slide--holding{top:892px}

/* title slide */
.hero{position:absolute;inset:0;background:linear-gradient(180deg,#2a7f9a 0%,#2c8ba6 55%,#3a95ad 100%)}
.hero__title{position:absolute;left:0;width:100%;padding-left:60px;top:118px;text-align:center;color:#fff;font-weight:800;font-size:46px;letter-spacing:1px;line-height:1}
.hero__sub{position:absolute;left:0;width:100%;padding-left:60px;top:176px;text-align:center;color:#fff;font-size:14px}

/* shared */
.slide-title{position:absolute;left:18px;top:14px;font-size:19px;font-weight:700;color:var(--navy);white-space:nowrap}
.slide-title .accent{color:var(--teal)}
.brand{position:absolute;right:19px;top:24px;font-weight:800;font-size:11px;color:#1a1a1a;display:flex;align-items:center;gap:3px}
.brand__dot{width:8px;height:8px;background:var(--teal)}
.footer-band{position:absolute;left:0;bottom:1px;width:100%;height:7px;background:var(--teal)}
.page-tab{position:absolute;right:0;bottom:0;width:66px;height:11px;background:var(--blue);clip-path:polygon(22% 0,100% 0,100% 100%,0 100%);color:#fff;font-size:6px;font-weight:700;text-align:right;padding-right:27px;line-height:11px}

/* table */
.pl{position:absolute;left:25px;top:52px;width:458px;border-collapse:collapse;font-size:4.6px;table-layout:fixed}
.pl td{height:7.6px;padding:0 1px;white-space:nowrap;line-height:7.6px}
.pl td.num{text-align:right}
.pl td.lbl{padding-left:4px}
.pl .head td{height:10px;color:#fff;font-weight:700;text-align:center;font-size:5px}
.pl .head .h-actual{background:var(--navy)}
.pl .head .h-budget{background:var(--teal-mid)}
.pl .head .h-var{background:var(--teal-light)}
.pl .section td{font-weight:700}
.pl .total td{font-weight:700}
.r-sales{background:#c9e1f2}
.r-sales-t{background:#b3d6ee;color:var(--navy)}
.r-prime{background:#e5f0ed}
.r-prime-t{background:#a9d6cd}
.r-op{background:#f0f0f0}
.r-op-t{background:#a8a8a8}
.r-nc{background:#d0d6dc}
.r-nc-t{background:#aab4bc}
.r-corp{background:#bcdcef}
.r-corp-t{background:#7fbce3}
.r-net{background:var(--navy);color:#fff}
.neg{color:var(--red)}

/* chart */
.chart{position:absolute;left:0;top:0;width:509px;height:280px}
.chart text{font-family:"Open Sans",Arial,sans-serif}

/* holding */
.holding__title{position:absolute;left:32px;top:76px;font-size:19px;font-weight:700;color:var(--navy);white-space:nowrap}
.holding__title .accent{color:var(--teal)}
.holding .brand{left:19px;right:auto;top:26px}
.holding__sub{position:absolute;left:36px;top:118px;font-size:9.5px;font-weight:700;color:var(--navy)}
.cash-list{position:absolute;left:38px;top:133px;list-style:none;font-size:7.6px;color:#333;line-height:11.6px}
.cash-list > li{padding-left:12px;position:relative}
.cash-list > li::before{content:"•";position:absolute;left:0}
.cash-list ul{list-style:none;padding-left:12px}
.cash-list ul li::before{content:"✓ ";}
.cash-list > li + li{margin-top:2px}
.photo{position:absolute;right:0;top:0;width:281px;height:280px;background:linear-gradient(135deg,#3a3432 0%,#7a5a4a 45%,#c8302c 75%,#e9e2dc 100%);clip-path:polygon(56% 0,100% 0,100% 100%,0 100%)}
</style>
</head>
<body>

<section class="slide slide--title">
  <div class="hero" role="img" aria-label="Photograph of a coastal road winding between green hills, tinted teal"></div>
  <h1 class="hero__title">RWP</h1>
  <p class="hero__sub">Quarter 2, 2021</p>
</section>

<section class="slide slide--budget">
  <h2 class="slide-title"><span class="accent">Qtr. Actual</span> vs Budget</h2>
  <div class="brand"><span class="brand__dot"></span>RWP</div>
  <table class="pl">
    <colgroup><col style="width:188px"><col style="width:56px"><col style="width:36px"><col style="width:53px"><col style="width:36px"><col style="width:52px"><col style="width:37px"></colgroup>
    <tr class="head"><td style="background:#fff"></td><td colspan="2" class="h-actual">Actual</td><td colspan="2" class="h-budget">Budget</td><td colspan="2" class="h-var">Variance B/-W</td></tr>
    <tr class="section"><td>Sales</td><td></td><td></td><td></td><td></td><td></td><td></td></tr>
    <tr class="r-sales"><td class="lbl">Sales</td><td class="num">4,479,434</td><td class="num">100.00%</td><td class="num">3,606,189</td><td class="num">100.00%</td><td class="num">873,245</td><td class="num">24.22%</td></tr>
    <tr class="r-sales-t total"><td>Total Sales</td><td class="num">4,479,434</td><td class="num">100.00%</td><td class="num">3,606,189</td><td class="num">100.00%</td><td class="num">873,245</td><td class="num">24.22%</td></tr>
    <tr class="section"><td>Prime Cost</td><td></td><td></td><td></td><td></td><td></td><td></td></tr>
    <tr class="r-prime"><td class="lbl">Cost of Sales</td><td class="num">1,273,991</td><td class="num">28.44%</td><td class="num">1,073,583</td><td class="num">29.77%</td><td class="num neg">-200,408</td><td class="num neg">-18.67%</td></tr>
    <tr class="r-prime"><td class="lbl">Personnel Costs</td><td class="num">1,344,279</td><td class="num">30.01%</td><td class="num">1,045,234</td><td class="num">28.98%</td><td class="num neg">-299,046</td><td class="num neg">-28.61%</td></tr>
    <tr class="r-prime-t total"><td>Total Prime Cost</td><td class="num">2,618,271</td><td class="num">58.45%</td><td class="num">2,118,817</td><td class="num">58.76%</td><td class="num neg">-499,454</td><td class="num neg">-23.57%</td></tr>
    <tr class="section"><td>Operating Expense</td><td></td><td></td><td></td><td></td><td></td><td></td></tr>
    <tr class="r-op total"><td>Restaurant Controllable Profit</td><td class="num">1,709,764</td><td class="num">38.17%</td><td class="num">1,365,221</td><td class="num">37.86%</td><td class="num">344,544</td><td class="num">25.24%</td></tr>
    <tr class="r-op"><td class="lbl">Controllable Expenses</td><td class="num">455,363</td><td class="num">10.17%</td><td class="num">357,438</td><td class="num">9.91%</td><td class="num neg">-97,926</td><td class="num neg">-27.4%</td></tr>
    <tr class="r-op"><td class="lbl">3rd Party Delivery Fees</td><td class="num">38,096</td><td class="num">0.85%</td><td></td><td></td><td class="num neg">-38,096</td><td class="num">0.0%</td></tr>
    <tr class="r-op"><td class="lbl">Advertising</td><td class="num">22,338</td><td class="num">0.50%</td><td class="num">16,024</td><td class="num">0.44%</td><td class="num neg">-6,314</td><td class="num neg">-39.4%</td></tr>
    <tr class="r-op"><td class="lbl">Other Expense</td><td class="num">595</td><td class="num">0.01%</td><td class="num">9,015</td><td class="num">0.25%</td><td class="num">8,420</td><td class="num">93.4%</td></tr>
    <tr class="r-op-t total"><td>Total Operating Expense</td><td class="num">516,392</td><td class="num">11.53%</td><td class="num">382,477</td><td class="num">10.61%</td><td class="num neg">-133,915</td><td class="num neg">-35.01%</td></tr>
    <tr class="section"><td>Non Controllable Expense</td><td></td><td></td><td></td><td></td><td></td><td></td></tr>
    <tr class="r-nc"><td class="lbl">Non-Controllable Expenses</td><td class="num">770,085</td><td class="num">17.19%</td><td class="num">712,459</td><td class="num">19.76%</td><td class="num neg">-57,626</td><td class="num neg">-8.09%</td></tr>
    <tr class="r-nc-t total"><td>Total Non Controllable Expense</td><td class="num">770,085</td><td class="num">17.19%</td><td class="num">712,459</td><td class="num">19.76%</td><td class="num neg">-57,626</td><td class="num neg">-8.09%</td></tr>
    <tr class="r-nc-t total"><td>Total Field Contribution</td><td class="num">574,687</td><td class="num">12.83%</td><td class="num">392,436</td><td class="num">10.88%</td><td class="num">182,251</td><td class="num">46.44%</td></tr>
    <tr class="section"><td>Corporate Overhead &amp; Other</td><td></td><td></td><td></td><td></td><td></td><td></td></tr>
    <tr class="r-corp"><td class="lbl">Interest Income</td><td></td><td></td><td class="num">131</td><td class="num">0.00%</td><td class="num">131</td><td class="num">100.0%</td></tr>
    <tr class="r-corp"><td class="lbl">Other Income</td><td class="num">-23</td><td class="num">0.00%</td><td class="num">31,651</td><td class="num">0.88%</td><td class="num">31,674</td><td class="num">100.07%</td></tr>
    <tr class="r-corp"><td class="lbl">Amortization</td><td></td><td></td><td></td><td></td><td></td><td class="num">0.0%</td></tr>
    <tr class="r-corp"><td class="lbl">Depreciation</td><td></td><td></td><td class="num">167,310</td><td class="num">4.64%</td><td class="num">167,310</td><td class="num">100.0%</td></tr>
    <tr class="r-corp-t total"><td>Total Corporate Overhead &amp; Other</td><td class="num">-23</td><td class="num">0.00%</td><td class="num">199,092</td><td class="num">5.52%</td><td class="num">199,115</td><td class="num">100.01%</td></tr>
    <tr class="r-net total"><td>Net Profit</td><td class="num">574,709</td><td class="num">12.83%</td><td class="num">193,344</td><td class="num">5.36%</td><td class="num">381,365</td><td class="num">197.25%</td></tr>
  </table>
  <div class="footer-band"></div>
  <div class="page-tab">2</div>
</section>

<section class="slide slide--cash">
  <h2 class="slide-title"><span class="accent">YTD Actual vs.</span> Projected Cash</h2>
  <div class="brand"><span class="brand__dot"></span>RWP</div>
  <svg class="chart" viewBox="0 0 509 280" aria-label="Line chart of cash projection versus cash balance, periods 1 to 7">
    <g stroke="#e4e4e4" stroke-width="0.6">
      <line x1="108" y1="70" x2="451" y2="70"/><line x1="108" y1="96.7" x2="451" y2="96.7"/>
      <line x1="108" y1="123.3" x2="451" y2="123.3"/><line x1="108" y1="150" x2="451" y2="150"/>
      <line x1="108" y1="176.7" x2="451" y2="176.7"/><line x1="108" y1="203.3" x2="451" y2="203.3"/>
      <line x1="108" y1="230" x2="451" y2="230"/>
    </g>
    <g font-size="5" fill="#333" text-anchor="end">
      <text x="103" y="72">$1,500,000</text><text x="103" y="98.7">$1,400,000</text>
      <text x="103" y="125.3">$1,300,000</text><text x="103" y="152">$1,200,000</text>
      <text x="103" y="178.7">$1,100,000</text><text x="103" y="205.3">$1,000,000</text>
      <text x="103" y="232">$900,000</text>
    </g>
    <text x="63" y="150" font-size="5" fill="#333" transform="rotate(-90 63 150)" text-anchor="middle">Dollars</text>
    <path d="M132 165.2 C150 167 165 169 181 168.3 C200 167 215 157 230 153.2 C248 148 262 142 279 136.6 C295 131 312 126 328 121.7 C345 116 360 103 377 105.2 C395 108 410 145 426 169" fill="none" stroke="var(--navy)" stroke-width="1.4"/>
    <path d="M132 198.3 C150 202 165 208 181 205.7 C200 200 215 186 230 175.5 C248 160 260 134 279 133.2 C297 132 312 145 328 140.8 C345 135 358 106 377 97.2 C395 87 410 78 426 69.5" fill="none" stroke="var(--teal)" stroke-width="1.4"/>
    <g fill="#fff" stroke="var(--navy)" stroke-width="0.8">
      <circle cx="132" cy="165.2" r="1.8"/><circle cx="181" cy="168.3" r="1.8"/><circle cx="230" cy="153.2" r="1.8"/>
      <circle cx="279" cy="136.6" r="1.8"/><circle cx="328" cy="121.7" r="1.8"/><circle cx="377" cy="105.2" r="1.8"/><circle cx="426" cy="169" r="1.8"/>
    </g>
    <g fill="#fff" stroke="var(--teal)" stroke-width="0.8">
      <circle cx="132" cy="198.3" r="1.8"/><circle cx="181" cy="205.7" r="1.8"/><circle cx="230" cy="175.5" r="1.8"/>
      <circle cx="279" cy="133.2" r="1.8"/><circle cx="328" cy="140.8" r="1.8"/><circle cx="377" cy="97.2" r="1.8"/><circle cx="426" cy="69.5" r="1.8"/>
    </g>
    <g stroke="#ccc" stroke-width="0.4" fill="none">
      <rect x="108" y="230" width="343" height="22"/>
      <line x1="108" y1="237" x2="451" y2="237"/><line x1="108" y1="244.5" x2="451" y2="244.5"/>
      <line x1="157" y1="230" x2="157" y2="252"/><line x1="206" y1="230" x2="206" y2="252"/>
      <line x1="255" y1="230" x2="255" y2="252"/><line x1="304" y1="230" x2="304" y2="252"/>
      <line x1="353" y1="230" x2="353" y2="252"/><line x1="402" y1="230" x2="402" y2="252"/>
      <line x1="60" y1="237" x2="108" y2="237"/><line x1="60" y1="244.5" x2="108" y2="244.5"/><line x1="60" y1="252" x2="108" y2="252"/>
    </g>
    <g font-size="4.4" fill="#333" text-anchor="middle">
      <text x="132" y="235.3">P 1</text><text x="181" y="235.3">P2</text><text x="230" y="235.3">P3</text><text x="279" y="235.3">P4</text><text x="328" y="235.3">P5</text><text x="377" y="235.3">P6</text><text x="426" y="235.3">P7</text>
      <text x="132" y="242.6">$1,143,090</text><text x="181" y="242.6">$1,131,558</text><text x="230" y="242.6">$1,187,848</text><text x="279" y="242.6">$1,250,190</text><text x="328" y="242.6">$1,306,052</text><text x="377" y="242.6">$1,368,051</text><text x="426" y="242.6">$1,128,802</text>
      <text x="132" y="250">$1,018,795</text><text x="181" y="250">$991,213</text><text x="230" y="250">$1,104,349</text><text x="279" y="250">$1,263,020</text><text x="328" y="250">$1,234,562</text><text x="377" y="250">$1,398,062</text><text x="426" y="250">$1,501,718</text>
    </g>
    <line x1="61" y1="241" x2="73" y2="241" stroke="var(--navy)" stroke-width="1.4"/><circle cx="67" cy="241" r="1.5" fill="#fff" stroke="var(--navy)" stroke-width="0.8"/>
    <line x1="61" y1="248.5" x2="73" y2="248.5" stroke="var(--teal)" stroke-width="1.4"/><circle cx="67" cy="248.5" r="1.5" fill="#fff" stroke="var(--teal)" stroke-width="0.8"/>
    <g font-size="4.4" fill="#333"><text x="74" y="242.6">Cash Projection</text><text x="74" y="250">Cash Balance</text></g>
  </svg>
  <div class="footer-band"></div>
  <div class="page-tab">3</div>
</section>

<section class="slide slide--holding holding">
  <div class="brand"><span class="brand__dot"></span>RWP</div>
  <h2 class="holding__title"><span class="accent">Current</span> Cash Holding</h2>
  <p class="holding__sub">Current Cash as of 8/25/21</p>
  <ul class="cash-list">
    <li>Harbor State Bank
      <ul><li>Checking: $1,532,893</li></ul>
    </li>
    <li>Prairie Trust Bank
      <ul><li>Money Market: $931,358</li><li>RWP DC Checking: $99,934</li></ul>
    </li>
    <li>Total Cash: $2,564,190</li>
    <li>2020 ERC Credit: $1,053,536
      <ul><li>Anticipated Deposit: Q1-22</li></ul>
    </li>
    <li>2021 ERC under review</li>
  </ul>
  <div class="photo" role="img" aria-label="Photograph of a smiling restaurant crew member in a red shirt and cap, kitchen staff behind"></div>
</section>

</body>
</html>
```